wardrobe/costume stylist needs good business card for own business

Hi:)

I'm wanting a business card for my company. I am a freelance stylist.

I do wardrobe/costume stylist to TV commercials; Films; Fashion and Lifestyle shoots.

I'd like a design based around my name Rosalind Darby written nicely, maybe a colour? Up to you?!

I've attached a couple of images of business cards I like
.... be creative and have fun!

Thank you :)
Updates

Reason: I was trying to get my new business card ready for before I headed overseas Friday morning but I don't think that was realistic so I'd like to extend the deadline to give time to the project. Thank you

Hi designers:) Thank you for all your designs, I've extended the deadline until Sunday, so there's a bit more time. I've attached 3 pictures of business cards which I quite like, please take a look to see if it can be of help in your process. I like the pale plain or patterned background with dark font and the dark plain or patterned background with the pale font the motifs the feminine fonts the plain fonts I like the idea of playing with a circle or some shape on one side of the card with my name or initials as in the picture I have on my post could you play around with this idea a bit please? Thank you all for the work you've done :) Rosie

Hi I am working overseas til Saturday night sorry for no feedback until I teturn Thanks :) Rosie

Hi designers, Thank you all so much for submitting your designs, I really appreciate your input into my project :) I'm sorry I didn't get to respond to some comments, and give feedback. I didn't back from being away until later than I expected, and the deadline had passed then, so apologies. Thanks to you all again for all your really good designs :) Rosie

Target Market(s)

I am a freelance stylist my target audience is producers, production companies, photographers, directors...

Industry/Entity Type

Business

Requirements
Must have
• Rosalind Darby
Stylist or Wardrobe Stylist

email rosiedarby@mailpeak.co.nz
Mobile 0218846193

(Don't have to use the words 'email' and 'mobile')
Nice to have
• Would like it to be double sided
Like B & W
Like pale colour background with dark font or white font
Like dark colour background with pale font
Should not have
• I would prefer it not to incorporate pictures

```html
<!DOCTYPE html>
<html lang="en">
<head>
<meta charset="utf-8">
<title>Rosalind Darby – Stylist business card</title>
<link rel="stylesheet" href="https://fonts.googleapis.com/css2?family=Pinyon+Script&family=Open+Sans:wght@300;400&display=swap">
<style>
  :root {
    --backdrop-light: #f4f4f4;
    --backdrop-dark: #d2d2d2;
    --card-stock: #bdb8ab;
    --ink-grey: #6d6d6b;
    --ink-white: #ffffff;
    --card-shadow: rgba(0, 0, 0, 0.16);
  }
  * { box-sizing: border-box; margin: 0; padding: 0; }
  html, body {
    width: 1200px;
    height: 1000px;
    overflow: hidden;
  }
  body {
    position: relative;
    background: radial-gradient(ellipse at 50% 40%, var(--backdrop-light) 0%, var(--backdrop-dark) 100%);
    font-family: "Open Sans", Arial, sans-serif;
  }
  .card {
    position: absolute;
    background: var(--card-stock);
    box-shadow: 0 3px 10px var(--card-shadow);
  }
  .card--back {
    left: 540px;
    top: 140px;
    width: 520px;
    height: 297px;
  }
  .card--front {
    left: 140px;
    top: 480px;
    width: 620px;
    height: 354px;
  }
  .studio-mark {
    position: absolute;
    font-family: "Open Sans", Arial, sans-serif;
    font-weight: 300;
    color: var(--ink-grey);
    letter-spacing: 0.04em;
    white-space: nowrap;
  }
  .card--back .studio-mark {
    left: 70px;
    top: 78px;
    font-size: 22px;
  }
  .contact {
    position: absolute;
    left: 70px;
    top: 124px;
    width: 180px;
    text-align: center;
    font-size: 12px;
    line-height: 20px;
    color: var(--ink-grey);
    font-weight: 400;
  }
  .card--front .studio-mark {
    right: 110px;
    top: 70px;
    font-size: 30px;
  }
  .holder-name {
    position: absolute;
    right: 70px;
    top: 128px;
    font-family: "Pinyon Script", "Times New Roman", serif;
    font-size: 46px;
    color: var(--ink-grey);
    white-space: nowrap;
  }
  .holder-role {
    position: absolute;
    right: 70px;
    top: 196px;
    font-size: 22px;
    font-weight: 300;
    color: var(--ink-white);
  }
</style>
</head>
<body>
  <section class="card card--back" aria-label="Card back">
    <div class="studio-mark">Darby Studio</div>
    <div class="contact">
      <p class="contact-email">rosiedarby@mailpeak.co.nz</p>
      <p class="contact-phone">0218846193</p>
    </div>
  </section>

  <section class="card card--front" aria-label="Card front">
    <div class="studio-mark">Darby Studio</div>
    <h1 class="holder-name">Rosalind Darby</h1>
    <p class="holder-role">Stylist</p>
  </section>
</body>
</html>
```